Saltwater Aquarium Store Business Cards

Im looking for a fresh new look to my out dated business cards for my company. Its a retail saltwater aquarium store. I want like a modern design that has an aquatic underwater feel. Needs to have certain business information as well. I would like to incorporate my logo as well. and a qr code for our website.
Logo Text
already have a logo

```html
<!DOCTYPE html>
<html lang="en">
<head>
<meta charset="utf-8">
<title>Coral Tide Aquatics – Business Card</title>
<link href="https://fonts.googleapis.com/css2?family=Lato:wght@400;700;900&display=swap" rel="stylesheet">
<style>
  :root {
    --page-bg: #e6e4e2;
    --card-light: #f4f3f4;
    --card-mid: #dcd9da;
    --navy: #16263a;
    --deep: #0d1726;
    --ocean-blue: #2a80c9;
    --band-blue: #4da2da;
    --coral-red: #d8433f;
    --reef-green: #8dc63f;
    --text-light: #f1f3f6;
  }
  * { margin: 0; padding: 0; box-sizing: border-box; }
  html, body { width: 1200px; height: 734px; overflow: hidden; }
  body {
    background: var(--page-bg);
    font-family: "Lato", sans-serif;
    position: relative;
  }
  .business-card {
    position: absolute;
    left: 30px; top: 40px;
    width: 1140px; height: 655px;
    border-radius: 28px;
    overflow: hidden;
    background: linear-gradient(160deg, var(--card-light) 0%, #ffffff 35%, var(--card-mid) 100%);
    box-shadow: 0 6px 20px rgba(0,0,0,0.12);
  }
  .card-art { position: absolute; inset: 0; }
  .brand {
    position: absolute;
    left: 60px; top: 90px;
    display: flex; align-items: center; gap: 18px;
  }
  .brand-dot {
    width: 64px; height: 64px; border-radius: 50%;
    background: var(--band-blue);
  }
  .brand-name {
    font-weight: 900; font-size: 54px; color: var(--navy);
    letter-spacing: 0.5px;
  }
  .person {
    position: absolute; right: 64px; top: 318px; text-align: right;
  }
  .person-name {
    font-weight: 700; font-size: 48px; color: var(--ocean-blue);
    letter-spacing: 0.5px; line-height: 1;
  }
  .person-title {
    font-size: 30px; color: var(--coral-red); margin-top: 8px; line-height: 1;
  }
  .contact-list {
    position: absolute; right: 58px; top: 450px;
    list-style: none; text-align: right;
  }
  .contact-item {
    display: flex; justify-content: flex-end; align-items: center;
    gap: 20px; color: var(--text-light); font-size: 26px; height: 40px;
  }
  .contact-item.phone { font-size: 30px; }
  .contact-icon { width: 22px; height: 22px; flex: none; }
</style>
</head>
<body>
  <div class="business-card">
    <svg class="card-art" viewBox="0 0 1140 655" width="1140" height="655">
      <defs>
        <linearGradient id="deepWater" x1="0" y1="0" x2="0" y2="1">
          <stop offset="0" stop-color="#1c2e44"/>
          <stop offset="0.6" stop-color="#132339"/>
          <stop offset="1" stop-color="var(--deep)"/>
        </linearGradient>
      </defs>
      <path d="M0,482 C300,530 520,420 690,318 C820,240 900,200 970,190 L1140,190 L1140,655 L0,655 Z" fill="#ffffff"/>
      <path d="M0,468 C300,515 520,400 690,300 C820,222 900,190 960,180" fill="none" stroke="var(--band-blue)" stroke-width="26"/>
      <path role="img" aria-label="Underwater reef scene with fish in deep blue water"
            d="M0,517 C300,560 520,440 700,322 C850,224 950,178 1060,184 C1100,188 1125,196 1140,204 L1140,655 L0,655 Z"
            fill="url(#deepWater)"/>
      <path d="M380,410 C560,340 700,240 850,192 C950,160 1050,150 1140,180" fill="none" stroke="#ffffff" stroke-width="22"/>
      <path d="M380,410 C560,340 700,240 850,192 C950,160 1050,150 1140,180" fill="none" stroke="var(--coral-red)" stroke-width="13"/>
      <path d="M30,455 C250,470 450,380 663,235" fill="none" stroke="var(--reef-green)" stroke-width="5"/>
    </svg>

    <div class="brand">
      <span class="brand-dot"></span>
      <span class="brand-name">Coral Tide Aquatics</span>
    </div>

    <div class="person">
      <div class="person-name">DANIEL REYES</div>
      <div class="person-title">Founder &amp; CEO</div>
    </div>

    <ul class="contact-list">
      <li class="contact-item phone">(123) 456-7890
        <svg class="contact-icon" viewBox="0 0 24 24"><path d="M6.6 10.8a15 15 0 0 0 6.6 6.6l2.2-2.2a1 1 0 0 1 1-.25 11.4 11.4 0 0 0 3.6.57 1 1 0 0 1 1 1V20a1 1 0 0 1-1 1A17 17 0 0 1 3 4a1 1 0 0 1 1-1h3.5a1 1 0 0 1 1 1c0 1.25.2 2.45.57 3.57a1 1 0 0 1-.25 1z" fill="var(--coral-red)"/></svg>
      </li>
      <li class="contact-item">store@coraltideaquatic.com
        <svg class="contact-icon" viewBox="0 0 24 24"><rect x="2" y="5" width="20" height="14" rx="1" fill="var(--coral-red)"/><path d="M2.5 6l9.5 7 9.5-7" fill="none" stroke="#ffffff" stroke-width="1.5"/></svg>
      </li>
      <li class="contact-item">www.coraltideaquatic.com
        <svg class="contact-icon" viewBox="0 0 24 24"><circle cx="12" cy="12" r="10" fill="var(--coral-red)"/><path d="M2 12h20M12 2c3 3 3 17 0 20M12 2c-3 3-3 17 0 20" fill="none" stroke="#ffffff" stroke-width="1.2"/></svg>
      </li>
      <li class="contact-item">Your Address, City, State, Country, Zip 1235
        <svg class="contact-icon" viewBox="0 0 24 24"><path d="M12 2a7 7 0 0 0-7 7c0 5 7 13 7 13s7-8 7-13a7 7 0 0 0-7-7z" fill="var(--coral-red)"/><circle cx="12" cy="9" r="2.6" fill="#ffffff"/></svg>
      </li>
    </ul>
  </div>
</body>
</html>
```